Switch Kit - Banking Flyer

We want a design for an 8.5x11" flyer that matches the look of our website (www.morvalecommercebank.com). Outline is attached, but please feel free to include images/pictures/graphics that you think makes this easy to understand. The goal is to hand this flyer to a potential customer to get them to understand the information easily and quickly.

```html
<!DOCTYPE html>
<html lang="en">
<head>
<meta charset="UTF-8">
<title>Switch Kit – Morvale Commerce Bank</title>
<link rel="stylesheet" href="https://fonts.googleapis.com/css2?family=Libre+Baskerville:wght@400;700&family=Montserrat:ital,wght@0,400;0,500;0,600;0,700;0,800;1,400&family=Oswald:wght@500&display=swap">
<style>
  :root {
    --navy: #3d4f6e;
    --navy-deep: #2f3e5a;
    --gold: #b08a4a;
    --band-blue: #dde5ec;
    --band-peach: #f6e6cf;
    --white: #ffffff;
    --page-bg: #d4d4d4;
    --serif: "Libre Baskerville", Georgia, serif;
    --sans: "Montserrat", Arial, sans-serif;
    --cond: "Oswald", "Arial Narrow", sans-serif;
  }
  * { box-sizing: border-box; margin: 0; padding: 0; }
  html, body { width: 1200px; height: 2295px; overflow: hidden; background: var(--page-bg); }
  .flyer {
    position: absolute; left: 40px; top: 423px;
    width: 1120px; height: 1449px;
    background: var(--white);
    box-shadow: 0 20px 40px rgba(0,0,0,.25);
    font-family: var(--sans); color: var(--navy-deep);
  }
  .band { position: absolute; left: 0; width: 100%; }
  .art { position: absolute; border-radius: 6px; }

  /* Header */
  .header { top: 0; height: 429px; background: linear-gradient(90deg, #3b4d6c 0%, #465a7c 100%); color: var(--white); }
  .welcome { position: absolute; left: 62px; top: 72px; font-family: var(--serif); font-weight: 700; font-size: 47px; letter-spacing: 1px; }
  .bank-name { position: absolute; left: 58px; top: 128px; font-family: var(--serif); font-weight: 700; font-size: 76px; color: var(--gold); letter-spacing: 1px; }
  .bank-sub { position: absolute; left: 62px; top: 222px; font-family: var(--serif); font-weight: 700; font-size: 36px; letter-spacing: 8px; }
  .rule { position: absolute; left: 62px; top: 283px; width: 428px; height: 1px; background: var(--gold); }
  .tag-small { position: absolute; left: 62px; top: 304px; font-size: 19px; letter-spacing: 4px; font-weight: 500; }
  .tag-big { position: absolute; left: 62px; top: 334px; font-size: 35px; font-weight: 800; line-height: 39px; }
  .logo { position: absolute; right: 62px; top: 58px; font-family: var(--serif); font-size: 27px; font-weight: 400; color: var(--white); letter-spacing: 2px; }
  .hero-art { left: 567px; top: 158px; width: 540px; height: 250px; background: linear-gradient(135deg, #8c86e0 0%, #a9a6f0 50%, #f2b233 100%); opacity: .85; }

  /* Steps */
  .step-1 { top: 437px; height: 222px; background: var(--band-blue); }
  .step-2 { top: 667px; height: 416px; background: var(--band-peach); }
  .step-3 { top: 1091px; height: 222px; background: var(--band-blue); }
  .badge { position: absolute; display: flex; align-items: center; }
  .badge svg { display: block; }
  .step-title { position: absolute; font-weight: 700; font-size: 21px; line-height: 25px; color: var(--navy); }
  .step-body { position: absolute; font-size: 17px; line-height: 20px; color: var(--navy-deep); }
  .bullets { position: absolute; left: 387px; top: 142px; width: 640px; list-style: none; font-size: 16.5px; line-height: 20px; }
  .bullets li { position: relative; padding-left: 18px; margin-bottom: 16px; }
  .bullets li::before { content: ""; position: absolute; left: 1px; top: 6px; width: 8px; height: 8px; border-radius: 50%; background: var(--navy); }
  .bullets em { font-style: italic; }
  .bullets b { font-weight: 700; }

  /* Footer */
  .footer { top: 1321px; height: 128px; background: var(--navy); color: var(--white); }
  .contact-label { position: absolute; left: 62px; top: 47px; font-size: 28px; font-weight: 800; }
  .contact-label span { color: var(--gold); }
  .contact-lines { position: absolute; left: 277px; top: 40px; font-size: 17px; line-height: 22px; }
  .contact-lines div, .address { display: flex; align-items: center; gap: 6px; }
  .address { position: absolute; left: 594px; top: 40px; font-size: 17px; line-height: 20px; align-items: flex-start; }
  .badges { position: absolute; right: 62px; top: 42px; display: flex; gap: 18px; }
  .badges span { display: block; width: 40px; height: 40px; border: 2px solid var(--white); border-radius: 4px; }
  .badges span + span { width: 66px; }
</style>
</head>
<body>
<main class="flyer">

  <section class="band header">
    <h1>
      <span class="welcome">WELCOME TO</span>
      <span class="bank-name">MORVALE</span>
      <span class="bank-sub">Commerce Bank!</span>
    </h1>
    <div class="rule"></div>
    <p class="tag-small">WE LOOK FORWARD TO CREAT</p>
    <p class="tag-big">AN EXCEPTIONAL<br>EXPERIENCE FOR YOU</p>
    <div class="logo">Morvale Commerce Bank</div>
    <div class="art hero-art" role="img" aria-label="Illustration of a bank building with people, gold coins, a credit card and a percent sign"></div>
  </section>

  <section class="band step-1">
    <div class="badge" style="left:62px;top:30px;">
      <svg width="210" height="64" viewBox="0 0 210 64" aria-hidden="true">
        <rect x="40" y="14" width="166" height="40" rx="20" fill="#3d4f6e"/>
        <circle cx="32" cy="32" r="31" fill="#b08a4a"/>
        <circle cx="30" cy="32" r="28" fill="#3d4f6e"/>
        <text x="30" y="45" text-anchor="middle" font-family="Oswald, sans-serif" font-size="36" fill="#fff">1</text>
        <text x="85" y="46" font-family="Oswald, sans-serif" font-size="32" fill="#fff" letter-spacing="1">STEP</text>
      </svg>
    </div>
    <h2 class="step-title" style="left:280px;top:36px;">Open a Morvale Commerce<br>Bank Account</h2>
    <p class="step-body" style="left:62px;top:125px;width:560px;">Stop by our branch and visit with our knowledgeable team to open your new account. We will be happy to assist you in choosing the right account for your banking needs.</p>
    <div class="art" style="left:647px;top:40px;width:411px;height:162px;background:linear-gradient(180deg,#c9d6e6 0%,#8fb1df 100%);" role="img" aria-label="Illustration of bank staff helping customers at service desks"></div>
  </section>

  <section class="band step-2">
    <div class="art" style="left:14px;top:83px;width:342px;height:267px;background:linear-gradient(180deg,#eef2f6 0%,#9fc2e6 100%);" role="img" aria-label="Illustration of customers queuing at a bank teller counter"></div>
    <div class="badge" style="left:367px;top:40px;">
      <svg width="210" height="64" viewBox="0 0 210 64" aria-hidden="true">
        <rect x="40" y="14" width="166" height="40" rx="20" fill="#3d4f6e"/>
        <circle cx="32" cy="32" r="31" fill="#b08a4a"/>
        <circle cx="30" cy="32" r="28" fill="#3d4f6e"/>
        <text x="30" y="45" text-anchor="middle" font-family="Oswald, sans-serif" font-size="36" fill="#fff">2</text>
        <text x="85" y="46" font-family="Oswald, sans-serif" font-size="32" fill="#fff" letter-spacing="1">STEP</text>
      </svg>
    </div>
    <h2 class="step-title" style="left:587px;top:46px;width:500px;">Stop using your old account &amp; redirect your automatic payments &amp; direct deposits</h2>
    <ul class="bullets">
      <li><em>It is important to remember to keep your old account open to ensure all your outstanding checks, deposits, and automatic withdrawals have cleared.</em></li>
      <li>We will provide you with a <b>Payments Checklist</b> to help you determine the companies you may need to notify of your account change so they can redirect any deposits or automatic withdrawals.</li>
      <li>Our <b>Direct Deposit Change Notification and Notification of Automatic Withdrawal Change</b> forms will easily allow companies to redirect your direct deposit(s) and automatic withdrawals to your new Morvale Commerce Bank account.</li>
    </ul>
  </section>

  <section class="band step-3">
    <div class="badge" style="left:62px;top:38px;">
      <svg width="210" height="64" viewBox="0 0 210 64" aria-hidden="true">
        <rect x="40" y="14" width="166" height="40" rx="20" fill="#3d4f6e"/>
        <circle cx="32" cy="32" r="31" fill="#b08a4a"/>
        <circle cx="30" cy="32" r="28" fill="#3d4f6e"/>
        <text x="30" y="45" text-anchor="middle" font-family="Oswald, sans-serif" font-size="36" fill="#fff">3</text>
        <text x="85" y="46" font-family="Oswald, sans-serif" font-size="32" fill="#fff" letter-spacing="1">STEP</text>
      </svg>
    </div>
    <h2 class="step-title" style="left:280px;top:58px;">Close your old account</h2>
    <p class="step-body" style="left:62px;top:133px;width:700px;">Now you are ready to switch. We will even provide an Account Closure Authorization form to close your old account. Any remaining account balance will be transferred to your Morvale Commerce Bank account.</p>
    <div class="art" style="left:805px;top:6px;width:255px;height:208px;background:linear-gradient(135deg,#d9434f 0%,#3f63c4 60%,#f2b233 100%);opacity:.8;" role="img" aria-label="Illustration of a person in an armchair using a large smartphone with coins and cash"></div>
  </section>

  <footer class="band footer">
    <p class="contact-label">CONTACT <span>US</span></p>
    <div class="contact-lines">
      <div>
        <svg width="16" height="16" viewBox="0 0 24 24" aria-hidden="true"><path fill="#b08a4a" d="M6.6 10.8a15 15 0 0 0 6.6 6.6l2.2-2.2a1 1 0 0 1 1-.25 11.4 11.4 0 0 0 3.6.57 1 1 0 0 1 1 1V20a1 1 0 0 1-1 1A17 17 0 0 1 3 4a1 1 0 0 1 1-1h3.5a1 1 0 0 1 1 1c0 1.25.2 2.45.57 3.57a1 1 0 0 1-.25 1z"/></svg>
        480.555.0142
      </div>
      <div>
        <svg width="16" height="16" viewBox="0 0 24 24" aria-hidden="true"><circle cx="12" cy="12" r="9" fill="none" stroke="#b08a4a" stroke-width="2.4"/><path d="M3 12h18M12 3c3 3 3 15 0 18M12 3c-3 3-3 15 0 18" fill="none" stroke="#b08a4a" stroke-width="1.8"/></svg>
        www.morvalecommercebank.com
      </div>
    </div>
    <div class="address">
      <svg width="16" height="20" viewBox="0 0 24 30" aria-hidden="true"><path fill="#b08a4a" d="M12 0a10 10 0 0 0-10 10c0 7.5 10 20 10 20s10-12.5 10-20A10 10 0 0 0 12 0zm0 14a4 4 0 1 1 0-8 4 4 0 0 1 0 8z"/></svg>
      <span>2740 Harlow Avenue,<br>Suite 310 Tempe, AZ 85281</span>
    </div>
    <div class="badges" aria-hidden="true"><span></span><span></span></div>
  </footer>

</main>
</body>
</html>
```